Online-Marketing Material für Bewegungsangebot speziell für Kinder
Zielgruppe
Hopsalino bietet ein hochwertiges, sportwissenschaftlich fundiertes Bewegungsangebot speziell für Kinder an. Unsere Kurse verbinden spielerische Elemente mit modernen Trainingsmethoden und schaffen eine liebevolle Umgebung in der Kinder ganz ohne Druck wachsen, lernen und sich mit Freude bewegen.
Unsere Zielgruppe sind Eltern mit Kindern zwischen zwei und acht Jahren, die ein qualitativ sehr hochwertiges Sportprogramm für ihre Kinder suchen und großen Wert auf professionelle Förderung, Sicherheit und eine warmherzige Atmosphäre legen.
Aufgabenstellung
Die Kreativen sollen berücksichtigen, dass der neue Hero ein echter Eye Catcher sein muss. Er soll sofort ein Wow-Gefühl auslösen und viel stärker auffallen als die aktuelle, eher schlichte Hero Section. Die Gestaltung soll hochwertig, kindlich liebevoll und gleichzeitig modern wirken. Der neue Hero muss sich perfekt in das bestehende Webdesign einfügen und die Hopsalino Welt auf den ersten Blick spürbar machen. Der bestehende Text bleibt zwingend erhalten. Alles andere darf kreativ neu gedacht werden, solange das Ergebnis direkt Aufmerksamkeit fängt, Emotionen weckt und die hohe Qualität des Sportangebots im Kindersegment sichtbar macht.
Ich benötige ein vollständiges Redesign ausschließlich für die Hero Section meiner Website www.hopsalino-kurse.example. Das restliche Webdesign passt bereits sehr gut zu meiner Marke, doch die aktuelle Hero Section wirkt noch zu schlicht und erzeugt kein echtes Wow-Gefühl.
Hopsalino steht für ein hochwertiges, sportwissenschaftlich fundiertes Sportangebot für Kinder zwischen zwei und acht Jahren. Unsere Welt ist liebevoll, warm, spielerisch und gleichzeitig sehr professionell. Genau dieses Gefühl soll der neue Hero sofort transportieren.
Wichtige Vorgaben
• Es geht ausschließlich um die Hero Section
• Der bestehende Text muss unbedingt erhalten bleiben
• Das Design soll hochwertig, kindlich, warm und liebevoll wirken
• Optisch nahtlose Anpassung an das bestehende Webdesign
• Der neue Hero soll ein klarer Eye Catcher sein und ein echtes Wow erzeugen
• Kreative Freiheit in der Gestaltung, solange alles modern, hochwertig und zur Hopsalino Welt passend bleibt
Mir ist wichtig, dass der neue Hero direkt Emotionen weckt und die hohe Qualität unseres Kinder-Sportangebots schon auf den ersten Blick spürbar macht.

```html
<!DOCTYPE html>
<html lang="de">
<head>
<meta charset="utf-8">
<title>Hopsalino – Ballschule &amp; Kurse</title>
<link href="https://fonts.googleapis.com/css2?family=Lato:wght@400;700;900&display=swap" rel="stylesheet">
<style>
:root{
  --sky:#33aee0;
  --sky-light:#bfe6f6;
  --sky-pale:#e6f6fc;
  --white:#ffffff;
  --ink:#222222;
  --gold:#e9c75e;
  --gold-line:#e2cf8c;
  --grey-soft:#efefef;
}
*{margin:0;padding:0;box-sizing:border-box}
html,body{width:1200px;height:1029px;overflow:hidden;background:var(--white);font-family:"Lato",sans-serif;color:var(--ink)}
.site-header{position:absolute;left:0;top:0;width:1200px;height:77px;background:var(--sky)}
.brand{position:absolute;left:188px;top:16px;color:var(--white);text-align:center}
.brand-name{display:block;font-weight:900;font-size:28px;letter-spacing:.5px;line-height:1}
.brand-sub{display:block;font-weight:400;font-size:11px;margin-top:2px;letter-spacing:.2px}
.main-nav{position:absolute;top:45px;left:0;width:1200px}
.main-nav a{position:absolute;color:var(--white);text-decoration:none;font-weight:700;font-size:12px;letter-spacing:.2px}
.hero{position:absolute;left:0;top:77px;width:1200px;height:609px;overflow:hidden;
  background:radial-gradient(circle at 50% 50%,var(--sky-pale) 0%,var(--sky-light) 45%,#9fd8f0 100%)}
.hero-ring{position:absolute;left:324px;top:29px;width:552px;height:552px;border-radius:50%;border:1px solid var(--gold-line)}
.hero-disc{position:absolute;left:330px;top:34px;width:542px;height:542px;border-radius:50%;
  background:linear-gradient(180deg,var(--white) 0%,var(--grey-soft) 100%);text-align:center}
.hero-mark{position:absolute;left:0;right:0;top:60px;display:flex;align-items:center;justify-content:center;gap:6px}
.hero-mark .dot{width:12px;height:12px;border-radius:50%;background:var(--gold)}
.hero-mark span{font-weight:900;font-size:16px;color:var(--ink);letter-spacing:.3px}
.hero-title{position:absolute;left:0;right:0;top:136px;color:var(--sky);font-weight:700;font-size:43px;line-height:52px}
.hero-text{position:absolute;left:75px;width:392px;top:258px;font-size:16.5px;line-height:20.6px}
.hero-text strong{font-weight:700}
.cta{position:absolute;left:177px;top:440px;width:187px;height:54px;border-radius:27px;background:var(--gold);
  color:var(--ink);text-decoration:none;font-size:12px;line-height:14.5px;display:flex;align-items:center;justify-content:center;text-transform:uppercase}
.gallery{position:absolute;left:0;top:686px;width:1200px;height:334px}
</style>
</head>
<body>
<header class="site-header">
  <div class="brand"><span class="brand-name">HOPSALINO</span><span class="brand-sub">BALLSCHULE &amp; KURSE</span></div>
  <nav class="main-nav">
    <a href="#" style="left:740px">KONZEPT</a>
    <a href="#" style="left:842px">FRANCHISE</a>
    <a href="#" style="left:955px">KONTAKT</a>
  </nav>
</header>

<section class="hero" role="img" aria-label="Hellblauer Strahlenkranz als Hintergrund">
  <div class="hero-ring"></div>
  <div class="hero-disc">
    <div class="hero-mark"><div class="dot"></div><span>HOPSALINO</span></div>
    <h1 class="hero-title">Deine Ballschule für<br>Kinder ab 2 Jahren</h1>
    <p class="hero-text">Stinkbomben ausweichen, Balli retten und ins Weltall fliegen. Bei Hopsalino werden Kinder nicht nur zu kleinen Bewegungsprofis, bei uns geht es um weit mehr. <strong>Motorik, Koordination und gezieltes Gehirntraining</strong> fördern die Entwicklung deines Kindes spielerisch und ganzheitlich in einer liebevollen Umgebung.</p>
    <a class="cta" href="#">Kurs in deiner<br>Nähe finden</a>
  </div>
</section>

<svg class="gallery" viewBox="0 800 1400 390" width="1200" height="334" preserveAspectRatio="none">
  <defs>
    <linearGradient id="grass" x1="0" y1="0" x2="0" y2="1"><stop offset="0" stop-color="#7fa06a"/><stop offset="1" stop-color="#2f5fb8"/></linearGradient>
    <linearGradient id="room" x1="0" y1="0" x2="0" y2="1"><stop offset="0" stop-color="#9a9a98"/><stop offset="1" stop-color="#6b5038"/></linearGradient>
    <linearGradient id="court" x1="0" y1="0" x2="0" y2="1"><stop offset="0" stop-color="#b9c7d2"/><stop offset=".4" stop-color="#6f8aa4"/><stop offset="1" stop-color="#2d63b0"/></linearGradient>
    <linearGradient id="garden" x1="0" y1="0" x2="0" y2="1"><stop offset="0" stop-color="#9fb48e"/><stop offset=".5" stop-color="#3a6fc0"/><stop offset="1" stop-color="#4f8a3a"/></linearGradient>
  </defs>
  <g role="img" aria-label="Foto: Kindergruppe mit Maskottchen auf der Wiese"><polygon points="99,890 153,905 153,1098 99,1112" fill="url(#grass)"/></g>
  <g role="img" aria-label="Foto: Kind umarmt das Bären-Maskottchen"><polygon points="193,880 345,895 345,1108 193,1122" fill="url(#room)"/></g>
  <g role="img" aria-label="Foto: Kinder auf dem Sportplatz mit Hütchen"><polygon points="344,871 563,885 563,1120 344,1131" fill="url(#court)"/></g>
  <g role="img" aria-label="Foto: Lachendes Kind im blauen Trikot"><rect x="563" y="866" width="269" height="270" fill="url(#garden)"/></g>
  <g role="img" aria-label="Foto: Trainer mit Kind und Bären-Maskottchen"><polygon points="832,885 1049,871 1049,1131 832,1120" fill="url(#room)"/></g>
  <g role="img" aria-label="Foto: Parcours mit Hütchen auf dem Sportplatz"><polygon points="1049,895 1198,880 1198,1122 1049,1108" fill="url(#court)"/></g>
  <g role="img" aria-label="Foto: Kindergruppe im Freien"><polygon points="1239,905 1291,897 1291,1110 1239,1098" fill="url(#grass)"/></g>
</svg>
</body>
</html>
```